Custom Mexican Train Dominos Scorecard

My wife and I regularly play Mexican Train dominos with our friends and family and would like to create a series of custom scorecards specific to our various groups that we play with. The idea would be to have them printed on pads or in notebooks that over time will hold a record of all of our games. Searching around on the web, the only "off the shelf" that I see are pretty plain and boring (see attached). We would love something with a fun and playful mid-century graphic feel to it. Can be a single color or more than one. We want to have the player names incorporated into the design, so for the first one the names would be Carla, Douglas, Ruth & Oliver. We will want a place to date each card and of course boxes to fill out the score. I have included a few examples of how the scorecard is basically laid out. Can be any size and can be done in landscape or portrait. I think I would just like the title to say "Domino Night" or potentially no title at all with just a fun domino graphic. Thank you!

Requirements
Must have
• Basic score layout
Nice to have
• nothing in particular
Should not have
• nothing in particular

```html
<!DOCTYPE html>
<html lang="en">
<head>
<meta charset="utf-8">
<title>Domino Night Scorecard</title>
<link rel="stylesheet" href="https://fonts.googleapis.com/css2?family=Federant&family=Rye&family=Titan+One&display=swap">
<style>
  :root {
    --ink: #1a1a1a;
    --paper: #ffffff;
    --ornament: #cfcfcf;
    --rule: #333333;
  }
  * { box-sizing: border-box; margin: 0; padding: 0; }
  html, body { width: 1200px; height: 1200px; overflow: hidden; background: var(--paper); }
  .scorecard { position: relative; width: 1200px; height: 1200px; color: var(--ink); }

  .title-panel {
    position: absolute; left: 207px; top: 56px; width: 876px; height: 202px;
    border: 2px solid var(--ink);
  }
  .title-panel .inner-frame {
    position: absolute; inset: 10px; border: 1.5px solid var(--ink);
  }
  .ornament { position: absolute; background: var(--ornament); border-radius: 6px; }
  .ornament.corner { width: 46px; height: 46px; }
  .ornament.tl { left: 14px; top: 14px; }
  .ornament.tr { right: 14px; top: 14px; }
  .ornament.bl { left: 14px; bottom: 14px; }
  .ornament.br { right: 14px; bottom: 14px; }
  .ornament.flank-l { left: 268px; top: 12px; width: 30px; height: 36px; }
  .ornament.flank-r { right: 268px; top: 12px; width: 30px; height: 36px; }
  .ornament.bottom-center { left: 368px; bottom: 12px; width: 140px; height: 28px; }
  .subtitle {
    position: absolute; left: 0; right: 0; top: 14px; text-align: center;
    font-family: "Rye", serif; font-size: 30px; letter-spacing: 3px;
  }
  .main-title {
    position: absolute; left: 0; right: 0; top: 50px; text-align: center;
    font-family: "Titan One", sans-serif; font-size: 92px; letter-spacing: 2px;
    text-shadow: 4px 4px 0 var(--paper), 7px 7px 0 var(--ink);
  }

  .names {
    position: absolute; left: 207px; top: 264px; width: 876px; height: 84px;
    display: grid; grid-template-columns: repeat(4, 1fr);
    border: 2px solid var(--ink);
  }
  .name-cell { position: relative; border-left: 1.5px solid var(--ink); }
  .name-cell:first-child { border-left: none; }
  .name-cell .nib { position: absolute; width: 16px; height: 16px; background: var(--ornament); border-radius: 3px; }
  .nib.a { left: 5px; top: 5px; } .nib.b { right: 5px; top: 5px; }
  .nib.c { left: 5px; bottom: 5px; } .nib.d { right: 5px; bottom: 5px; }
  .name-oval {
    position: absolute; left: 6px; right: 6px; top: 12px; bottom: 10px;
    border: 2px solid var(--ink); border-radius: 50%; background: var(--paper);
    display: flex; align-items: center; justify-content: center;
    font-family: "Federant", serif; font-size: 40px; letter-spacing: 1px;
  }

  .score-table {
    position: absolute; left: 94px; top: 348px; width: 989px;
    border-collapse: collapse; table-layout: fixed;
    border: 2px solid var(--ink);
  }
  .score-table col.label { width: 113px; }
  .score-table td { border: 1.3px solid var(--rule); height: 49px; }
  .score-table td.round { text-align: center; vertical-align: middle; }
  .score-table tr.subtotal td { height: 40px; border-top: 4px double var(--ink); border-bottom: 4px double var(--ink); }
  .score-table tr.total td { height: 56px; border-top: 2px solid var(--ink); }
  .row-label {
    font-family: "Titan One", sans-serif; font-size: 16px; text-align: center; letter-spacing: 0.5px;
  }
  .total .row-label { font-size: 24px; }
  .total .entry { padding: 4px; }
  .total .entry span { display: block; height: 100%; min-height: 44px; border: 2.5px solid var(--ink); }
  .domino { width: 68px; height: 26px; display: inline-block; vertical-align: middle; }
</style>
</head>
<body>
<svg width="0" height="0" style="position:absolute" aria-hidden="true">
  <defs>
    <symbol id="p0" viewBox="0 0 30 20"></symbol>
    <symbol id="p1" viewBox="0 0 30 20"><circle cx="15" cy="10" r="1.7"/></symbol>
    <symbol id="p2" viewBox="0 0 30 20"><circle cx="7" cy="5" r="1.7"/><circle cx="23" cy="15" r="1.7"/></symbol>
    <symbol id="p3" viewBox="0 0 30 20"><use href="#p2"/><circle cx="15" cy="10" r="1.7"/></symbol>
    <symbol id="p4" viewBox="0 0 30 20"><circle cx="7" cy="5" r="1.7"/><circle cx="23" cy="5" r="1.7"/><circle cx="7" cy="15" r="1.7"/><circle cx="23" cy="15" r="1.7"/></symbol>
    <symbol id="p5" viewBox="0 0 30 20"><use href="#p4"/><circle cx="15" cy="10" r="1.7"/></symbol>
    <symbol id="p6" viewBox="0 0 30 20"><use href="#p4"/><circle cx="7" cy="10" r="1.7"/><circle cx="23" cy="10" r="1.7"/></symbol>
    <symbol id="p7" viewBox="0 0 30 20"><use href="#p6"/><circle cx="15" cy="10" r="1.7"/></symbol>
    <symbol id="p8" viewBox="0 0 30 20"><use href="#p6"/><circle cx="15" cy="5" r="1.7"/><circle cx="15" cy="15" r="1.7"/></symbol>
    <symbol id="p9" viewBox="0 0 30 20"><use href="#p8"/><circle cx="15" cy="10" r="1.7"/></symbol>
    <symbol id="p10" viewBox="0 0 30 20"><circle cx="5" cy="5" r="1.6"/><circle cx="11.7" cy="5" r="1.6"/><circle cx="18.3" cy="5" r="1.6"/><circle cx="25" cy="5" r="1.6"/><circle cx="5" cy="15" r="1.6"/><circle cx="11.7" cy="15" r="1.6"/><circle cx="18.3" cy="15" r="1.6"/><circle cx="25" cy="15" r="1.6"/><circle cx="5" cy="10" r="1.6"/><circle cx="25" cy="10" r="1.6"/></symbol>
    <symbol id="p11" viewBox="0 0 30 20"><use href="#p10"/><circle cx="15" cy="10" r="1.6"/></symbol>
    <symbol id="p12" viewBox="0 0 30 20"><use href="#p10"/><circle cx="11.7" cy="10" r="1.6"/><circle cx="18.3" cy="10" r="1.6"/></symbol>
    <symbol id="tile" viewBox="0 0 68 26"><rect x="1" y="1" width="66" height="24" rx="3" fill="#fff" stroke="#1a1a1a" stroke-width="1.5"/><line x1="34" y1="4" x2="34" y2="22" stroke="#1a1a1a" stroke-width="1.2"/></symbol>
  </defs>
</svg>

<main class="scorecard">
  <header class="title-panel">
    <div class="inner-frame"></div>
    <div class="ornament corner tl" role="img" aria-label="Corner flourish ornament"></div>
    <div class="ornament corner tr" role="img" aria-label="Corner flourish ornament"></div>
    <div class="ornament corner bl" role="img" aria-label="Corner flourish ornament"></div>
    <div class="ornament corner br" role="img" aria-label="Corner flourish ornament"></div>
    <div class="ornament flank-l" role="img" aria-label="Scroll ornament"></div>
    <div class="ornament flank-r" role="img" aria-label="Scroll ornament"></div>
    <div class="ornament bottom-center" role="img" aria-label="Centre scroll ornament"></div>
    <p class="subtitle">MEXICAN TRAIN</p>
    <h1 class="main-title">DOMINO NIGHT</h1>
  </header>

  <section class="names">
    <div class="name-cell"><i class="nib a"></i><i class="nib b"></i><i class="nib c"></i><i class="nib d"></i><div class="name-oval">CARLA</div></div>
    <div class="name-cell"><i class="nib a"></i><i class="nib b"></i><i class="nib c"></i><i class="nib d"></i><div class="name-oval">DOUGLAS</div></div>
    <div class="name-cell"><i class="nib a"></i><i class="nib b"></i><i class="nib c"></i><i class="nib d"></i><div class="name-oval">RUTH</div></div>
    <div class="name-cell"><i class="nib a"></i><i class="nib b"></i><i class="nib c"></i><i class="nib d"></i><div class="name-oval">OLIVER</div></div>
  </section>

  <table class="score-table">
    <colgroup><col class="label"><col><col><col><col></colgroup>
    <tr><td class="round"><svg class="domino" viewBox="0 0 68 26" aria-label="Double twelve"><use href="#tile"/><use href="#p12" x="3" y="3" width="30" height="20"/><use href="#p12" x="35" y="3" width="30" height="20"/></svg></td><td></td><td></td><td></td><td></td></tr>
    <tr><td class="round"><svg class="domino" viewBox="0 0 68 26" aria-label="Double eleven"><use href="#tile"/><use href="#p11" x="3" y="3" width="30" height="20"/><use href="#p11" x="35" y="3" width="30" height="20"/></svg></td><td></td><td></td><td></td><td></td></tr>
    <tr><td class="round"><svg class="domino" viewBox="0 0 68 26" aria-label="Double ten"><use href="#tile"/><use href="#p10" x="3" y="3" width="30" height="20"/><use href="#p10" x="35" y="3" width="30" height="20"/></svg></td><td></td><td></td><td></td><td></td></tr>
    <tr><td class="round"><svg class="domino" viewBox="0 0 68 26" aria-label="Double nine"><use href="#tile"/><use href="#p9" x="3" y="3" width="30" height="20"/><use href="#p9" x="35" y="3" width="30" height="20"/></svg></td><td></td><td></td><td></td><td></td></tr>
    <tr><td class="round"><svg class="domino" viewBox="0 0 68 26" aria-label="Double eight"><use href="#tile"/><use href="#p8" x="3" y="3" width="30" height="20"/><use href="#p8" x="35" y="3" width="30" height="20"/></svg></td><td></td><td></td><td></td><td></td></tr>
    <tr><td class="round"><svg class="domino" viewBox="0 0 68 26" aria-label="Double seven"><use href="#tile"/><use href="#p7" x="3" y="3" width="30" height="20"/><use href="#p7" x="35" y="3" width="30" height="20"/></svg></td><td></td><td></td><td></td><td></td></tr>
    <tr class="subtotal"><td class="row-label">SUB TOTAL</td><td></td><td></td><td></td><td></td></tr>
    <tr><td class="round"><svg class="domino" viewBox="0 0 68 26" aria-label="Double six"><use href="#tile"/><use href="#p6" x="3" y="3" width="30" height="20"/><use href="#p6" x="35" y="3" width="30" height="20"/></svg></td><td></td><td></td><td></td><td></td></tr>
    <tr><td class="round"><svg class="domino" viewBox="0 0 68 26" aria-label="Double five"><use href="#tile"/><use href="#p5" x="3" y="3" width="30" height="20"/><use href="#p5" x="35" y="3" width="30" height="20"/></svg></td><td></td><td></td><td></td><td></td></tr>
    <tr><td class="round"><svg class="domino" viewBox="0 0 68 26" aria-label="Double four"><use href="#tile"/><use href="#p4" x="3" y="3" width="30" height="20"/><use href="#p4" x="35" y="3" width="30" height="20"/></svg></td><td></td><td></td><td></td><td></td></tr>
    <tr><td class="round"><svg class="domino" viewBox="0 0 68 26" aria-label="Double three"><use href="#tile"/><use href="#p3" x="3" y="3" width="30" height="20"/><use href="#p3" x="35" y="3" width="30" height="20"/></svg></td><td></td><td></td><td></td><td></td></tr>
    <tr><td class="round"><svg class="domino" viewBox="0 0 68 26" aria-label="Double two"><use href="#tile"/><use href="#p2" x="3" y="3" width="30" height="20"/><use href="#p2" x="35" y="3" width="30" height="20"/></svg></td><td></td><td></td><td></td><td></td></tr>
    <tr><td class="round"><svg class="domino" viewBox="0 0 68 26" aria-label="Double one"><use href="#tile"/><use href="#p1" x="3" y="3" width="30" height="20"/><use href="#p1" x="35" y="3" width="30" height="20"/></svg></td><td></td><td></td><td></td><td></td></tr>
    <tr><td class="round"><svg class="domino" viewBox="0 0 68 26" aria-label="Double blank"><use href="#tile"/></svg></td><td></td><td></td><td></td><td></td></tr>
    <tr class="subtotal"><td class="row-label">SUB TOTAL</td><td></td><td></td><td></td><td></td></tr>
    <tr class="total"><td class="row-label">TOTAL</td><td class="entry"><span></span></td><td class="entry"><span></span></td><td class="entry"><span></span></td><td class="entry"><span></span></td></tr>
  </table>
</main>
</body>
</html>
```